Harbor Nightclub

Nightclub flyer., digital single sided, for KV and PX. I included samples of some previous flyers we've used. Sample Info:
HARBOR
FRIDAYS
FRI MAY 1 2020
DJ VORTAN (club floor)
DJ RUZO & DJ TAV (residents on the lounge floor)
4217 Marlow Avenue Sacramento
www.harborvenuehall.example for list/VIP inquiries

Target Market(s)

Upscale top 40 crowd but want some cool and artsy like the examples included.

Font styles to use
Sans Serif

Requirements
Must have
• Harbor Logo
Nice to have
• Would be nice if the flyer can be incorporated later with DJ photos (sometimes we will add dj photos to pixagram etc). Would like a big city type of feel.
Should not have
• Nothing too sexual.

```html
<!DOCTYPE html>
<html lang="en">
<head>
<meta charset="utf-8">
<title>Harbor Fridays</title>
<link rel="stylesheet" href="https://fonts.googleapis.com/css2?family=Montserrat:wght@600;700;800;900&display=swap">
<style>
  :root {
    --ink: #000000;
    --gold: #f0a92a;
    --gold-light: #ffd36a;
    --gold-deep: #c9821a;
    --night: #070504;
    --ember: #5a0c06;
    --photo-light: #cfcfcf;
    --photo-dark: #2a2a2a;
  }
  html, body {
    margin: 0;
    width: 1200px;
    height: 1200px;
    overflow: hidden;
    background: var(--ink);
  }
  .flyer {
    position: relative;
    width: 1200px;
    height: 1200px;
    font-family: "Montserrat", sans-serif;
    color: var(--gold);
    overflow: hidden;
  }
  .city-backdrop {
    position: absolute;
    inset: 0;
    background:
      radial-gradient(ellipse 520px 200px at 220px 1080px, rgba(120,20,10,0.55), transparent 70%),
      radial-gradient(ellipse 600px 260px at 900px 260px, rgba(90,14,8,0.45), transparent 70%),
      radial-gradient(ellipse 500px 300px at 300px 200px, rgba(60,10,6,0.5), transparent 70%),
      var(--night);
  }
  .brand-mark {
    position: absolute;
    left: 0; right: 0;
    top: 52px;
    display: flex;
    flex-direction: column;
    align-items: center;
  }
  .brand-dot {
    width: 200px;
    height: 200px;
    border-radius: 50%;
    background: var(--gold-deep);
  }
  .brand-name {
    margin-top: 34px;
    font-weight: 600;
    font-size: 80px;
    line-height: 1;
    letter-spacing: 2px;
    color: var(--gold);
  }
  .night-title {
    position: absolute;
    left: 0; right: 0;
    top: 424px;
    text-align: center;
    font-weight: 900;
    font-size: 162px;
    line-height: 1;
    letter-spacing: 2px;
    background: linear-gradient(180deg, var(--gold-light), var(--gold) 55%, var(--gold-deep));
    -webkit-background-clip: text;
    background-clip: text;
    color: transparent;
  }
  .event-date {
    position: absolute;
    left: 0; right: 0;
    top: 592px;
    text-align: center;
    font-weight: 800;
    font-size: 42px;
    letter-spacing: 10px;
    color: var(--gold);
  }
  .lineup {
    position: absolute;
    left: 0; top: 0;
    width: 1200px;
    height: 1200px;
  }
  .dj-name {
    position: absolute;
    top: 898px;
    font-weight: 700;
    font-size: 22px;
    color: var(--gold);
    text-align: center;
  }
  .dj-name.club { left: 200px; width: 300px; }
  .dj-name.lounge { left: 570px; width: 360px; }
  .divider {
    position: absolute;
    left: 350px;
    width: 500px;
    height: 2px;
    background: linear-gradient(90deg, transparent, var(--gold), transparent);
  }
  .divider.upper { top: 962px; }
  .divider.lower { top: 1076px; }
  .venue-address {
    position: absolute;
    left: 0; right: 0;
    top: 984px;
    text-align: center;
    font-weight: 800;
    font-size: 30px;
    line-height: 38px;
    letter-spacing: 8px;
    color: var(--gold);
  }
  .venue-site {
    position: absolute;
    left: 0; right: 0;
    top: 1118px;
    text-align: center;
    font-weight: 800;
    font-size: 30px;
    letter-spacing: 7px;
    color: var(--gold);
  }
</style>
</head>
<body>
<main class="flyer">
  <div class="city-backdrop" role="img" aria-label="Dark night-time city street photograph with red lights and a sprinkle of gold sparkle"></div>

  <div class="brand-mark">
    <div class="brand-dot"></div>
    <div class="brand-name">HARBOR</div>
  </div>

  <h1 class="night-title" style="margin:0;">FRIDAYS</h1>
  <div class="event-date">FRI MAY 1 2020</div>

  <svg class="lineup" viewBox="0 0 1200 1200" aria-hidden="false">
    <defs>
      <linearGradient id="photoTone" x1="0" y1="0" x2="1" y2="0">
        <stop offset="0" stop-color="var(--photo-dark)"/>
        <stop offset="0.55" stop-color="var(--photo-light)"/>
        <stop offset="1" stop-color="var(--photo-dark)"/>
      </linearGradient>
      <linearGradient id="frameGold" x1="0" y1="0" x2="1" y2="1">
        <stop offset="0" stop-color="#ffd36a"/>
        <stop offset="0.5" stop-color="#c9821a"/>
        <stop offset="1" stop-color="#ffd36a"/>
      </linearGradient>
    </defs>
    <g class="dj-photo club">
      <polygon points="300,678 556,678 482,888 226,888" fill="url(#photoTone)" role="img" aria-label="Portrait photo of the club floor DJ"/>
      <polygon points="300,678 556,678 482,888 226,888" fill="none" stroke="url(#frameGold)" stroke-width="6"/>
    </g>
    <g class="dj-photo lounge">
      <polygon points="680,678 926,678 852,888 606,888" fill="url(#photoTone)" role="img" aria-label="Portrait photo of the lounge floor resident DJs"/>
      <polygon points="680,678 926,678 852,888 606,888" fill="none" stroke="url(#frameGold)" stroke-width="6"/>
    </g>
  </svg>

  <div class="dj-name club">DJ VORTAN</div>
  <div class="dj-name lounge">DJ RUZO &amp; DJ TAV</div>

  <div class="divider upper"></div>
  <div class="venue-address">4217 MARLOW AVENUE<br>SACRAMENTO</div>
  <div class="divider lower"></div>

  <div class="venue-site">WWW.HARBORVENUEHALL.EXAMPLE</div>
</main>
</body>
</html>
```